Copper Lantern Podcast Business Card Design

Needing a business card with the logo design provided for Copper Lantern Podcast. I am looking for a modern style that fits the current logo.

Info:
Name: Bao Khanh
Title: Creator/Host
Email: bao@copperlanternpod.com
Phone: (405) 637-2918
www.copperlanternpod.com
Twitter: @coplanternpod
Instagram: @copperlanternpodcast
Facebook: Copper Lantern Podcast

Industry/Entity Type

Business

Font styles to use
Sans Serif

Colors
000000
ffffff

Requirements
Must have
• modern, clean design
Nice to have
• social media contact info

```html
<!DOCTYPE html>
<html lang="en">
<head>
<meta charset="utf-8">
<title>Copper Lantern Podcast – Business Card</title>
<link rel="stylesheet" href="https://fonts.googleapis.com/css2?family=Poppins:wght@400&family=Archivo:wght@600&display=swap">
<style>
  :root {
    --ink: #1c1a1b;
    --paper: #ffffff;
    --backdrop: #e9e9e9;
    --card-dark: #1d1d1d;
    --card-dark-glow: #3a3a3a;
    --silver: #a9a9a9;
    --shadow: rgba(0, 0, 0, 0.22);
  }
  * { box-sizing: border-box; margin: 0; padding: 0; }
  html, body {
    width: 1200px;
    height: 1000px;
    overflow: hidden;
    background: var(--backdrop);
  }
  .stage {
    position: relative;
    width: 1200px;
    height: 1000px;
  }
  .card {
    position: absolute;
    left: 240px;
    width: 696px;
    height: 396px;
    border-radius: 22px;
    box-shadow: 0 4px 10px var(--shadow);
  }
  .card-front { top: 82px; background: var(--paper); }
  .card-back {
    top: 520px;
    background: radial-gradient(ellipse at 50% 30%, var(--card-dark-glow) 0%, var(--card-dark) 60%);
  }

  .brand-name {
    position: absolute;
    font-family: "Archivo", "Helvetica Neue", Arial, sans-serif;
    font-weight: 600;
    text-transform: uppercase;
    text-align: center;
    line-height: 1.05;
  }
  .card-front .brand-name {
    left: 40px;
    width: 284px;
    top: 138px;
    font-size: 30px;
    color: var(--ink);
  }
  .card-back .brand-name {
    left: 0;
    width: 696px;
    top: 130px;
    font-size: 40px;
    color: var(--silver);
  }

  .divider {
    position: absolute;
    left: 336px;
    top: 104px;
    width: 2px;
    height: 190px;
    background: var(--ink);
  }

  .contact {
    position: absolute;
    left: 363px;
    top: 98px;
    font-family: "Poppins", "Helvetica Neue", Arial, sans-serif;
    color: var(--ink);
  }
  .contact-name {
    font-size: 23px;
    letter-spacing: 1px;
    text-transform: uppercase;
    line-height: 1.2;
  }
  .contact-title {
    font-size: 14px;
    letter-spacing: 0.5px;
    text-transform: uppercase;
    margin-bottom: 18px;
  }
  .contact-list { list-style: none; font-size: 15px; line-height: 21px; }
  .contact-list li { display: flex; align-items: center; gap: 11px; }
  .contact-list .gap { margin-top: 8px; }
  .icon { width: 13px; height: 13px; flex: none; fill: var(--ink); }
  .social-mark {
    width: 11px; height: 11px; flex: none;
    background: var(--ink);
    border-radius: 2px;
    margin: 0 1px;
  }
</style>
</head>
<body>
<main class="stage">
  <section class="card card-front" aria-label="Card front">
    <div class="brand-name">Copper<br>Lantern<br>Podcast</div>
    <div class="divider"></div>
    <div class="contact">
      <p class="contact-name">Bao Khanh</p>
      <p class="contact-title">Creator/Host</p>
      <ul class="contact-list">
        <li>
          <svg class="icon" viewBox="0 0 16 16" aria-hidden="true"><path d="M3.6 1.2 6 3.8 4.8 5.6c.9 2.2 3.3 4.6 5.6 5.6L12.2 10l2.6 2.4-1.6 2.4C7.6 14.4 1.6 8.4 1.2 2.8Z"/></svg>
          (405) 637-2918
        </li>
        <li>
          <svg class="icon" viewBox="0 0 16 16" aria-hidden="true"><path d="M1 3h14v1.2L8 8.6 1 4.2Zm0 2.6 7 4.4 7-4.4V13H1Z"/></svg>
          bao@copperlanternpod.com
        </li>
        <li>
          <svg class="icon" viewBox="0 0 16 16" aria-hidden="true"><circle cx="8" cy="8" r="6.5" fill="none" stroke="#1c1a1b" stroke-width="1.5"/><path d="M1.5 8h13M8 1.5c-3 3.5-3 9.5 0 13M8 1.5c3 3.5 3 9.5 0 13" fill="none" stroke="#1c1a1b" stroke-width="1.2"/></svg>
          www.copperlanternpod.com
        </li>
        <li class="gap"><span class="social-mark"></span>Copper Lantern Podcast</li>
        <li><span class="social-mark"></span>@coplanternpod</li>
        <li><span class="social-mark"></span>@copperlanternpodcast</li>
      </ul>
    </div>
  </section>

  <section class="card card-back" aria-label="Card back">
    <div class="brand-name">Copper<br>Lantern<br>Podcast</div>
  </section>
</main>
</body>
</html>
```